Dana's Business Card Design

I am in need of a business card design for our company Tolleshunt Wrecking & Reclaim (WA) Pty Ltd. Apart from being licenced demolition contractors for residential, commercial or industrial projects we have a 20 acre salvage yard full of recycled building materials, we are also licenced to remove Asbestos and we have our own recycling/refuge tip and this site is also licenced to take Asbestos contamination landfill,we also have a sandpit in which we sell sand. Our primary colour is blue and we have a little man logo which i will attach that has been our logo for the good part of the last thirty years so this is to be included, I wont mind if you alter/update him in any way although his tattoo's must remain.
Target Market(s)
Construction & Building Industry
Industry/Entity Type
Industrial
Contact Information for Business Card
TOLLESHUNT WRECKING & RECLAIM (WA) PTY LTD
Dana Tolleshunt
Credit Controller/Payroll Officer
2417 Felmore Ridge Road
LOWER ELDERGATE  WA  6071
PH: 0428 615 704
Fax: (08) 9371 5820
dana@twreck.example.com.au
tolleshuntwrecking.example.com.au

```html
<!DOCTYPE html>
<html lang="en">
<head>
<meta charset="utf-8">
<title>Dana Tolleshunt – Business Card</title>
<link rel="stylesheet" href="https://fonts.googleapis.com/css2?family=Questrial&display=swap">
<style>
  :root {
    --paper: #ffffff;
    --band-light: #e6f2fb;
    --band-mid: #d6e9f7;
    --navy: #1c1f9e;
    --name-blue: #2d62e6;
    --title-blue: #2233b0;
    --dash-blue: #6d93d6;
    --icon-purple: #a43ec4;
    --mascot-shirt: #3b6fe0;
    --mascot-skin: #dcc8ec;
    --mascot-shorts: #1f2aa8;
  }
  html, body {
    margin: 0;
    padding: 0;
    width: 1200px;
    height: 741px;
    overflow: hidden;
    background: var(--paper);
  }
  .card {
    position: relative;
    width: 1200px;
    height: 741px;
    background: var(--paper);
    font-family: "Questrial", sans-serif;
    overflow: hidden;
  }
  .card__backdrop {
    position: absolute;
    inset: 0;
  }
  .company {
    position: absolute;
    right: 101px;
    top: 109px;
    margin: 0;
    text-align: right;
    font-weight: 400;
    font-size: 38px;
    line-height: 37px;
    letter-spacing: -1.2px;
    color: var(--navy);
  }
  .person {
    position: absolute;
    left: 100px;
    top: 258px;
  }
  .person__name {
    margin: 0;
    font-weight: 400;
    font-size: 55px;
    line-height: 60px;
    letter-spacing: -1.8px;
    color: var(--name-blue);
  }
  .person__title {
    margin: 6px 0 0;
    font-size: 28px;
    line-height: 32px;
    letter-spacing: -0.9px;
    color: var(--title-blue);
  }
  .person__rule {
    display: block;
    margin-top: 6px;
  }
  .contacts {
    position: absolute;
    left: 100px;
    top: 444px;
    margin: 0;
    padding: 0;
    list-style: none;
  }
  .contacts__item {
    display: flex;
    align-items: center;
    height: 31.5px;
    font-size: 20px;
    letter-spacing: -0.7px;
    color: var(--navy);
  }
  .contacts__icon {
    flex: none;
    width: 26px;
    height: 26px;
    margin-right: 8px;
    border-radius: 50%;
    background: var(--icon-purple);
    color: #fff;
    font-size: 18px;
    line-height: 24px;
    text-align: center;
    letter-spacing: 0;
  }
  .mascot {
    position: absolute;
    left: 872px;
    top: 362px;
    width: 245px;
    height: 295px;
    border-radius: 48% 48% 42% 42%;
    background:
      radial-gradient(ellipse 55% 30% at 42% 28%, var(--mascot-shirt) 0%, rgba(59,111,224,0) 100%),
      radial-gradient(ellipse 45% 18% at 40% 58%, var(--mascot-shorts) 0%, rgba(31,42,168,0) 100%),
      radial-gradient(ellipse 50% 50% at 45% 50%, var(--mascot-skin) 40%, rgba(220,200,236,0) 100%);
  }
</style>
</head>
<body>
<main class="card">
  <svg class="card__backdrop" width="1200" height="741" viewBox="0 0 1200 741" aria-hidden="true">
    <path class="swoosh swoosh--top" d="M0 0 H630 C420 40 170 120 0 212 Z" fill="var(--band-light)"/>
    <path class="swoosh swoosh--bottom" d="M0 648 C330 640 820 560 1200 315 V741 H0 Z" fill="var(--band-mid)"/>
    <path class="swoosh swoosh--sheen" d="M0 648 C330 640 820 560 1200 315 V350 C850 560 400 650 0 662 Z" fill="#ffffff" opacity="0.55"/>
  </svg>

  <h1 class="company">TOLLESHUNT WRECKING &amp; RECLAIM<br>(WA) PTY LTD</h1>

  <section class="person">
    <h2 class="person__name">Dana Tolleshunt</h2>
    <p class="person__title">Credit Controller/Payroll Officer</p>
    <svg class="person__rule" width="372" height="6" viewBox="0 0 372 6" aria-hidden="true">
      <line x1="0" y1="3" x2="372" y2="3" stroke="var(--dash-blue)" stroke-width="5" stroke-dasharray="16 9"/>
    </svg>
  </section>

  <ul class="contacts">
    <li class="contacts__item"><span class="contacts__icon">a</span>2417 Felmore Ridge Road LOWER ELDERGATE WA 6071</li>
    <li class="contacts__item"><span class="contacts__icon">p</span>PH: 0428 615 704</li>
    <li class="contacts__item"><span class="contacts__icon">f</span>Fax: (08) 9371 5820</li>
    <li class="contacts__item"><span class="contacts__icon">e</span>dana@twreck.example.com.au</li>
    <li class="contacts__item"><span class="contacts__icon">w</span>tolleshuntwrecking.example.com.au</li>
  </ul>

  <div class="mascot" role="img" aria-label="Company mascot: tattooed demolition worker in hard hat, blue shirt and shorts, swinging a sledgehammer"></div>
</main>
</body>
</html>
```